Church Website with Home Page and Member Sermon Library

I am in need of an updated design for our church website. This will include 4 pages (outlined below). We are a conservative, evangelical, Christian church. The site should be modern and clean, while still reflecting our conservative values. I already have a logo for our church, and I want the site to incorporate the logo, and match the logo/branding. Stock photos are allowed if needed, but I have uploaded some images of our church and would prefer those images to be used if possible. Any stock photos used should not include any people in the photos (scenery, nature, buildings, animals, etc. are fine).

The site will need 4 pages: Home, Support Us (Donate), Login, and Recording Library.

Page 1: Home
The home page should include the following sections:

- Navigation: Should include links to each section of the home page plus a "listen live" link which will take the user to a live-streaming site and a "support us" link which will take the user to a support/donate page.

- Announcements: Can be either a banner or some other design, but there needs to be some way for us to post announcements for visitors to see. I'm open for creative ideas in this section, but would like it not to take up a lot of room on the page.

- About Us: Should include address, service times (see attached document), and information about the church.

- Pastor Bio: A section that introduces our pastor and gives a short bio about our pastor. Would like this section to include a picture of our pastor. Somewhere in this section I would like to include this Bible reference: "And I will give you pastors according to mine heart, which shall feed you with knowledge and understanding. Jer 3:15 KJV"

- Articles of Faith (What We Believe): This should include several sub-sections each with a heading, body, and possibly 1 or more scripture references. I have attached a document to the brief that includes our articles of faith. Feel free to be creative with this section in how you lay these out and format them.

- Support Us: A small section that explains what kind of support someone can give and a link to a donation page. The link can say something like "Support Us" or "Donate Now".

- Contact form: A contact form that allows the visitor to send us a message. The contact form should ask for name, email, phone, and message.

- Footer: A footer that will be displayed on all pages of the site. This should include at a minimum a link to the home page (or a link to each individual section in the home page if you prefer), a link to "listen live", a link to "support us", a link to "contact us" (or you can put the contact form directly in the footer if you prefer), the address, and a "member login" link.

Page 2: Support Us
The donation page should include a form the visitor can fill out to make a donation. We will embed a third party form later. For this design, please just mock out the design with a basic form asking for name, phone, and email.

Page 3: Login
The recording library (detailed below) will require members to login with a shared numeric code before accessing the page. We need a design for a login screen. The screen should include navigation/footer just like all other pages, but the body of the login page will consist only of a form that asks the user to enter the access code and then a "login" button.

Page 4: Recording Library

The library page is a member-only page that will require a shared, numeric pass code to access. On this page, members will be able to access a filterable list of past sermons. The page by default should display most recent sermons, but should also include a search form that allows the member to filter the sermon list to find a particular sermon. The search form should allow the user to select a filter type (e.g. Speaker name, date, event, etc.) and type in a value to search. They should be able to add multiple filters and remove filters that have been added. Each sermon that is displayed in the result list should include basic information such as title, date, speaker, tags, etc. along with a download icon, and an embedded audio player where they can click a play button to stream it on-demand. Each sermon should also have clickable tags associated with it that can be used to find related sermons.
Updates

I have uploaded several images of our church. Feel free to incorporate these into your design if possible.

Target Market(s)

Church Members

Industry/Entity Type

Religion

Number of Pages Required

4 page

Font styles to use
Sans Serif

Colors

Designer to choose colors to be used in the design.

Requirements
Must have
• Must incorporate the logo (attached)
Nice to have
• Would like the design to incorporate pictures of our church (attached) instead of stock photos if possible.
Should not have
• Please avoid an overly cluttered design. Stock photos used should not include any people in the photos.

```html
<!DOCTYPE html>
<html lang="en">
<head>
<meta charset="utf-8">
<title>Library – Cedar Grove Chapel</title>
<link href="https://fonts.googleapis.com/css2?family=Cinzel:wght@400;600;700&family=Montserrat:wght@400;500;600&display=swap" rel="stylesheet">
<style>
:root{
  --green:#7fae6a;
  --green-dark:#2f5530;
  --teal:#2aa7c2;
  --ink:#1e1e1e;
  --muted:#8a8a8a;
  --line:#dcdcdc;
  --panel:#f2f2f2;
  --dark:#2f2f2f;
  --white:#ffffff;
}
*{box-sizing:border-box;margin:0;padding:0}
html,body{width:1200px;height:2844px;overflow:hidden}
body{position:relative;background:var(--white);font-family:'Montserrat',sans-serif;color:var(--ink)}
.abs{position:absolute}
.serif{font-family:'Cinzel',serif}

/* hero */
.hero-photo{left:0;top:0;width:1200px;height:454px;
  background:linear-gradient(180deg,rgba(255,255,255,.95) 0%,rgba(255,255,255,0) 22%),
  linear-gradient(120deg,#c79a70 0%,#e0b48a 30%,#f3ddc6 55%,#b98054 80%,#7a4e30 100%)}
.brand{left:140px;top:60px;width:160px;text-align:center;font-family:'Cinzel',serif;font-size:19px;letter-spacing:2px;color:var(--green)}
.brand-mark{left:202px;top:20px;width:34px;height:34px;border:2px solid var(--teal)}
.nav{right:174px;top:34px;display:flex;gap:56px;font-size:16px;font-weight:500}
.page-title{left:0;width:1200px;top:238px;text-align:center;font-family:'Cinzel',serif;font-size:58px;letter-spacing:4px;color:#151515}
.title-rule{left:519px;top:317px;width:162px;height:3px;background:#151515}
.title-rule.short{left:560px;top:324px;width:80px;height:1px}

/* search */
.search-card{left:172px;top:416px;width:856px;height:73px;background:var(--white);box-shadow:0 6px 18px rgba(0,0,0,.08)}
.filter-type{left:181px;top:427px;width:150px;height:52px;background:var(--panel);font-size:16px;letter-spacing:1px;color:#555;display:flex;align-items:center;padding-left:25px;gap:12px}
.search-input{left:331px;top:427px;width:557px;height:52px;border:1px solid #e6e6e6;display:flex;align-items:center;padding-left:20px;gap:8px;font-size:14px;color:#aaa}
.add-filter{left:888px;top:427px;width:131px;height:52px;background:var(--green);color:#fff;font-weight:600;font-size:15px;display:flex;align-items:center;justify-content:center;letter-spacing:.5px}
.chip{top:508px;height:33px;border:1px solid #cfcfcf;border-radius:17px;font-size:14px;letter-spacing:1.5px;color:#444;display:flex;align-items:center;padding:0 16px;gap:10px}

/* sermon cards */
.sermon{width:416px;height:258px;color:#fff;overflow:hidden}
.sermon-photo{position:absolute;inset:0;background:linear-gradient(180deg,#cfd6cb 0%,#8fa284 35%,#3f6a3b 65%,#2a5228 100%)}
.sermon-photo.alt{background:linear-gradient(180deg,#e7ebe3 0%,#a8b7a0 30%,#467241 62%,#2b5429 100%)}
.sermon .download{position:absolute;left:19px;top:18px;font-size:12px;display:flex;gap:6px;align-items:center;opacity:.9}
.sermon .date{position:absolute;left:19px;top:135px;font-size:11px;display:flex;gap:5px;align-items:center}
.sermon .name{position:absolute;left:19px;top:151px;font-family:'Cinzel',serif;font-weight:700;font-size:14.5px;letter-spacing:1px}
.sermon .desc{position:absolute;left:20px;top:172px;width:270px;font-size:10px;line-height:12px;opacity:.9}
.sermon .by{position:absolute;left:19px;top:206px;font-size:12px;display:flex;align-items:center;gap:9px}
.avatar{width:22px;height:22px;border-radius:50%;background:#c9b8a8;border:1px solid #fff}
.sermon .tags{position:absolute;left:19px;top:229px;font-size:12px;display:flex;align-items:center;gap:4px}
.tag{border:1px solid #fff;border-radius:11px;padding:2px 8px;letter-spacing:1px}
.play{position:absolute;left:324px;top:120px;width:70px;height:70px;border-radius:50%;background:rgba(255,255,255,.35);border:2px solid rgba(255,255,255,.5);display:flex;align-items:center;justify-content:center}

.player{width:416px;height:258px;overflow:hidden;background:#2a2a2a}
.player-photo{position:absolute;left:0;top:0;width:416px;height:200px;background:linear-gradient(180deg,#f4f4f2 0%,#dcdad4 55%,#8c8c88 100%)}
.player-time{position:absolute;top:183px;font-size:10px;color:#fff}
.track{position:absolute;left:0;top:202px;width:416px;height:2px;background:#777}
.track-fill{position:absolute;left:0;top:202px;width:283px;height:2px;background:var(--green)}
.knob{position:absolute;left:275px;top:195px;width:16px;height:16px;border-radius:50%;background:#fff}

/* pagination */
.pager{left:536px;top:1462px;display:flex;align-items:center;gap:10px;font-family:'Cinzel',serif;font-size:12px}
.pager-box{width:33px;height:31px;border:1px solid #e2e2e2;display:flex;align-items:center;justify-content:center;color:var(--green)}

/* support + contact background */
.church-photo{left:0;top:1480px;width:1200px;height:1364px;
  background:linear-gradient(180deg,#ffffff 0%,#dfe1e5 8%,#b9a48f 30%,#7e5a43 48%,#4a3a31 58%,var(--dark) 68%,var(--dark) 100%)}
.section-title{left:0;width:1200px;text-align:center;font-family:'Cinzel',serif;letter-spacing:4px}
.support-btn{left:524px;top:1652px;width:149px;height:43px;background:var(--green);color:#fff;font-family:'Cinzel',serif;font-size:15px;display:flex;align-items:center;justify-content:center;gap:8px}
.rule-teal{left:550px;top:2093px;width:100px;height:3px;background:var(--teal)}
.field{background:#fff;border:1px solid #ccc;font-size:12px;color:#555;padding:22px 16px 0}
.send{left:534px;top:2378px;width:130px;height:46px;background:var(--green);color:#fff;font-family:'Cinzel',serif;font-size:15px;display:flex;align-items:center;justify-content:center;gap:10px}

/* footer */
.listen{left:177px;top:2573px;width:220px;height:64px;border-radius:32px;background:#f5f3ec;border:2px solid var(--green);box-shadow:0 6px 16px rgba(0,0,0,.35);display:flex;align-items:center;gap:30px;padding-left:6px;font-family:'Cinzel',serif;color:var(--green);font-size:16px}
.listen-icon{width:48px;height:48px;border-radius:50%;background:var(--green);display:flex;align-items:center;justify-content:center}
.foot-head{font-family:'Cinzel',serif;color:#ddd;font-size:16px;letter-spacing:1px}
.foot-text{color:#ccc;font-size:14px}
.foot-brand{left:400px;width:400px;top:2655px;text-align:center;font-family:'Cinzel',serif;font-size:34px;letter-spacing:3px;color:var(--green)}
.foot-mark{left:582px;top:2590px;width:36px;height:36px;border:2px solid var(--teal)}
.quick a{display:block;color:#ccc;text-decoration:none;font-size:14px;line-height:27.7px}
.social{left:911px;top:2790px;display:flex;gap:16px}
.social span{width:13px;height:13px;border-radius:50%;background:#fff}
</style>
</head>
<body>

<!-- hero -->
<div class="abs hero-photo" role="img" aria-label="Photo of wooden church pews"></div>
<div class="abs brand-mark"></div>
<div class="abs brand">Cedar Grove Chapel</div>
<nav class="abs nav"><span>About Us</span><span>Articles Of Faith</span><span>Contact Us</span></nav>
<h1 class="abs page-title">LIBRARY</h1>
<div class="abs title-rule"></div>
<div class="abs title-rule short"></div>

<!-- search -->
<div class="abs search-card"></div>
<div class="abs filter-type">SPEAKER
  <svg width="10" height="6" viewBox="0 0 10 6"><path d="M1 1l4 4 4-4" fill="none" stroke="#555" stroke-width="1.5"/></svg></div>
<div class="abs search-input">
  <svg width="13" height="13" viewBox="0 0 13 13"><circle cx="5" cy="5" r="4" fill="none" stroke="#aaa" stroke-width="1.5"/><path d="M8 8l4 4" stroke="#aaa" stroke-width="1.5"/></svg>
  Type your request here</div>
<div class="abs add-filter">ADD FILTER</div>
<div class="abs chip" style="left:181px">EVENT: Wedding <span>✕</span></div>
<div class="abs chip" style="left:380px">SPEAKER: Joel Whitfield <span>✕</span></div>

<!-- sermon grid -->
<article class="abs sermon" style="left:172px;top:570px">
  <div class="sermon-photo" role="img" aria-label="Photo of a pastor reading at the pulpit"></div>
  <div class="download">⤓ Download</div>
  <div class="date">▣ Fab 12, 2023</div>
  <div class="name">ULLAMCORPER FACILISI EGESTAS</div>
  <div class="desc">Ut diam tortor consectetur lacus scelerisque tortor congue viverra egestas.</div>
  <div class="by"><span class="avatar"></span>by: Mara Ellington</div>
  <div class="tags">search tags: <span class="tag">Ullamcorper facilis</span><span class="tag">facilis</span><span class="tag">Ullamcorper</span></div>
  <div class="play"><svg width="18" height="20" viewBox="0 0 18 20"><path d="M2 1l15 9-15 9z" fill="#fff"/></svg></div>
</article>

<article class="abs sermon" style="left:613px;top:570px">
  <div class="sermon-photo alt" role="img" aria-label="Photo of a pastor in a bright sanctuary"></div>
  <div class="download">⤓ Download</div>
  <div class="date">▣ Fab 12, 2023</div>
  <div class="name">ULLAMCORPER FACILISI EGESTAS</div>
  <div class="desc">Ut diam tortor consectetur lacus scelerisque tortor congue viverra egestas.</div>
  <div class="by"><span class="avatar"></span>by: Mara Ellington</div>
  <div class="tags">search tags: <span class="tag">Ullamcorper facilis</span><span class="tag">facilis</span><span class="tag">Ullamcorper</span></div>
  <div class="play" style="top:130px;left:330px"><svg width="18" height="20" viewBox="0 0 18 20"><path d="M2 1l15 9-15 9z" fill="#fff"/></svg></div>
</article>

<article class="abs sermon" style="left:172px;top:851px">
  <div class="sermon-photo alt" role="img" aria-label="Photo of a pastor in a bright sanctuary"></div>
  <div class="download">⤓ Download</div>
  <div class="date">▣ Fab 12, 2023</div>
  <div class="name">ULLAMCORPER FACILISI EGESTAS</div>
  <div class="desc">Ut diam tortor consectetur lacus scelerisque tortor congue viverra egestas.</div>
  <div class="by"><span class="avatar"></span>by: Mara Ellington</div>
  <div class="tags">search tags: <span class="tag">Ullamcorper facilis</span><span class="tag">facilis</span><span class="tag">Ullamcorper</span></div>
  <div class="play"><svg width="18" height="20" viewBox="0 0 18 20"><path d="M2 1l15 9-15 9z" fill="#fff"/></svg></div>
</article>

<article class="abs player" style="left:613px;top:851px">
  <div class="player-photo" role="img" aria-label="Photo of a pastor reading at the pulpit"></div>
  <div class="player-time" style="left:10px">23:25</div>
  <div class="player-time" style="right:10px">20:41</div>
  <div class="track"></div><div class="track-fill"></div><div class="knob"></div>
  <svg class="abs" style="left:155px;top:224px" width="110" height="16" viewBox="0 0 110 16">
    <path d="M2 2v12M14 2L5 8l9 6z" fill="#fff" stroke="#fff" stroke-width="2"/>
    <path d="M50 2v12M56 2v12" stroke="#fff" stroke-width="2"/>
    <path d="M108 2v12M96 2l9 6-9 6z" fill="#fff" stroke="#fff" stroke-width="2"/>
  </svg>
  <svg class="abs" style="left:383px;top:225px" width="16" height="14" viewBox="0 0 16 14"><path d="M1 5h3l4-4v12l-4-4H1z" fill="#ddd"/><path d="M11 4q2 3 0 6M13 2q4 5 0 10" fill="none" stroke="#ddd" stroke-width="1.3"/></svg>
</article>

<article class="abs sermon" style="left:172px;top:1133px">
  <div class="sermon-photo" role="img" aria-label="Photo of a pastor reading at the pulpit"></div>
  <div class="download">⤓ Download</div>
  <div class="date">▣ Fab 12, 2023</div>
  <div class="name">ULLAMCORPER FACILISI EGESTAS</div>
  <div class="desc">Ut diam tortor consectetur lacus scelerisque tortor congue viverra egestas.</div>
  <div class="by"><span class="avatar"></span>by: Mara Ellington</div>
  <div class="tags">search tags: <span class="tag">Ullamcorper facilis</span><span class="tag">facilis</span><span class="tag">Ullamcorper</span></div>
  <div class="play" style="top:128px"><svg width="18" height="20" viewBox="0 0 18 20"><path d="M2 1l15 9-15 9z" fill="#fff"/></svg></div>
</article>

<article class="abs sermon" style="left:613px;top:1133px">
  <div class="sermon-photo alt" role="img" aria-label="Photo of a pastor in a bright sanctuary"></div>
  <div class="download">⤓ Download</div>
  <div class="date" style="left:22px">▣ Fab 12, 2023</div>
  <div class="name" style="left:20px">ULLAMCORPER FACILISI EGESTAS</div>
  <div class="desc" style="left:22px">Ut diam tortor consectetur lacus scelerisque tortor congue viverra egestas.</div>
  <div class="by"><span class="avatar"></span>by: Mara Ellington</div>
  <div class="tags">search tags: <span class="tag">Ullamcorper facilis</span><span class="tag">facilis</span><span class="tag">Ullamcorper</span></div>
  <div class="play" style="top:120px;left:324px"><svg width="18" height="20" viewBox="0 0 18 20"><path d="M2 1l15 9-15 9z" fill="#fff"/></svg></div>
</article>

<!-- pagination -->
<div class="abs pager">
  <svg width="10" height="16" viewBox="0 0 10 16"><path d="M8 1L2 8l6 7" fill="none" stroke="#ccc" stroke-width="1.5"/></svg>
  <span class="pager-box">1</span><span>of <b>16</b></span>
  <svg width="10" height="16" viewBox="0 0 10 16"><path d="M2 1l6 7-6 7" fill="none" stroke="var(--green)" stroke-width="2"/></svg>
</div>

<!-- support & contact -->
<div class="abs church-photo" role="img" aria-label="Photo of the brick church building exterior"></div>
<h2 class="abs section-title" style="top:1570px;font-size:48px;color:#151515">SUPPORT OUR MINISTRY</h2>
<div class="abs support-btn">
  <svg width="20" height="20" viewBox="0 0 20 20"><rect x="3" y="2" width="12" height="15" fill="none" stroke="#fff" stroke-width="1.3"/><path d="M6 7h6M6 10h6M6 13h4" stroke="#fff" stroke-width="1.3"/></svg>
  SUPPORT US</div>

<h2 class="abs section-title" style="top:2040px;font-size:36px;color:#fff">CONTACT US</h2>
<div class="abs rule-teal"></div>
<div class="abs field" style="left:174px;top:2132px;width:417px;height:44px;padding-top:14px">Name *</div>
<div class="abs field" style="left:609px;top:2132px;width:413px;height:44px;padding-top:14px">Phone *</div>
<div class="abs field" style="left:174px;top:2190px;width:848px;height:44px;padding-top:14px">Email address *</div>
<div class="abs field" style="left:174px;top:2248px;width:848px;height:106px;padding-top:12px">Message</div>
<div class="abs send">SEND US
  <svg width="20" height="10" viewBox="0 0 20 10"><path d="M0 5h18M14 1l4 4-4 4" fill="none" stroke="#fff" stroke-width="1.5"/></svg></div>

<!-- footer -->
<div class="abs listen">
  <span class="listen-icon"><svg width="26" height="20" viewBox="0 0 26 20"><circle cx="13" cy="8" r="2.5" fill="#fff"/><path d="M8 3q-4 5 0 10M18 3q4 5 0 10" fill="none" stroke="#fff" stroke-width="1.5"/><rect x="8" y="15" width="10" height="5" fill="#fff"/></svg></span>
  LISTEN LIVE</div>
<div class="abs foot-head" style="left:184px;top:2670px">LOCATION</div>
<div class="abs foot-text" style="left:184px;top:2700px;width:250px;display:flex;gap:8px">
  <svg width="10" height="14" viewBox="0 0 10 14" style="flex:none;margin-top:2px"><path d="M5 13S1 8 1 5a4 4 0 018 0c0 3-4 8-4 8z" fill="none" stroke="var(--green)" stroke-width="1.3"/><circle cx="5" cy="5" r="1.4" fill="var(--green)"/></svg>
  <span>418 Orchard Lane, Millbrook, Ohio 43210</span></div>

<div class="abs foot-mark"></div>
<div class="abs foot-brand">Cedar Grove Chapel</div>

<div class="abs foot-head" style="left:825px;top:2563px">QUICK LINKS</div>
<nav class="abs quick" style="left:825px;top:2596px">
  <a href="#">About Us</a><a href="#">Articles Of Faith</a><a href="#">Support Our Ministry</a><a href="#">Contact Us</a><a href="#">Member Login</a>
</nav>

<div class="abs foot-text" style="left:176px;top:2797px;font-size:13px">Copyright 2023 Cedar Grove Chapel I All rights reserved</div>
<div class="abs social"><span></span><span></span><span></span><span></span></div>

</body>
</html>
```